Website design for an events management company

What we need is the design of a website to be used by an events management company, the company is called "Vanto Events Management" and the website is expected to contain the following sections:
1) Homepage
2) Who are we?
3) Mission / Vision / Core values
4) Why to choose Vanto?
5) Past experience
6) Duties or provided services (Scientific Program Duties, Accreditation, Fund Raising, Accommodations, Social Activities, Transportation, Marketing of the Event, Publications and printed materials, Secretarial Work and Media Coverage)
7) References
8) Contact Us page (will probably contain a contact us form plus email, address and a google map)

Attached for your reference the company's logo

Expected that the winner should deliver the designs of at least two pages (the homepage plus an inner page) plus of course all the used graphics, images ... etc.

Thanks

Target Market(s)

The design need to target scientific events and not public events, for example the company doesn't organize music concerts ... etc., it organizes only scientific events so please target business users (i.e. doctors, engineers, scientisits ... etc) while making the designs, including the correct colors, images and icons

Industry/Entity Type

It Company

Number of Pages Required

2 page

Requirements
Must have
• One homepage
• One inner page
• All the used graphics and images
Nice to have
• More than two pages

```html
<!DOCTYPE html>
<html lang="en">
<head>
<meta charset="utf-8">
<title>Vanto Events Management</title>
<link href="https://fonts.googleapis.com/css2?family=Mulish:wght@400;600;700&display=swap" rel="stylesheet">
<style>
:root{
  --blue:#4ab3e3;
  --ink:#2b2b2b;
  --grey-tile:#5e5e62;
  --nav:#545458;
  --footer:#5f5f62;
  --footer-dark:#4c4c4f;
  --line:#d8d8d8;
  --white:#ffffff;
  --muted:#e4e4e4;
  --red:#e03030;
}
*{box-sizing:border-box;margin:0;padding:0}
html,body{width:910px;height:1200px;overflow:hidden;background:var(--white)}
body{position:relative;font-family:"Mulish",sans-serif;color:var(--ink)}
.abs{position:absolute}

/* header */
.brand{left:77px;top:14px;width:100px}
.brand-mark{display:flex;align-items:center;gap:6px}
.brand-dot{width:14px;height:14px;border-radius:50%;background:var(--blue)}
.brand-name{font-size:30px;font-weight:700;color:var(--nav);line-height:1}
.brand-sub{font-size:7px;color:var(--nav);margin-top:6px;white-space:nowrap}
.contact{top:16px;right:76px;display:flex;gap:14px;font-size:12.5px;color:#555}
.contact span{display:flex;align-items:center;gap:6px}
.contact .ico{width:20px;height:20px;background:var(--blue);display:flex;align-items:center;justify-content:center}
.nav{left:186px;top:52px;width:650px;height:25px;background:var(--nav);display:flex}
.nav a{flex:1 1 auto;text-align:center;color:var(--white);font-size:10px;font-weight:600;text-decoration:none;padding:0 7px;line-height:25px;border-right:1px solid #6a6a6e;white-space:nowrap;letter-spacing:.2px}
.nav a:last-child{border-right:none}
.nav a.active{background:var(--blue)}

/* hero */
.hero{left:0;top:92px;width:910px;height:358px;background:linear-gradient(180deg,#d9d6cc 0%,#8b7a66 35%,#5a4636 70%,#3c3028 100%)}
.hero-arrow{top:250px}
.caption{left:0;top:411px;width:910px;height:39px;background:rgba(70,70,72,.75);color:var(--white);font-size:20px;line-height:39px;padding-left:74px}
.caption b{font-weight:700}
.dots{right:77px;top:427px;display:flex;gap:6px}
.dots i{width:7px;height:7px;border:1px solid var(--white)}
.dots i.on{background:var(--white)}

/* services */
.svc-title{left:0;top:476px;width:910px;text-align:center;font-size:24px;font-weight:700}
.svc-title span{color:var(--blue)}
.divider{left:200px;top:521px;width:510px;height:1px;background:var(--line)}
.divider-dot{left:447px;top:516px;width:11px;height:11px;border-radius:50%;border:2px solid var(--blue);background:var(--white)}
.svc-intro{left:70px;top:541px;width:770px;text-align:center;font-size:14.5px;line-height:21.5px;color:#333}
.tile{width:77px;height:78px;background:var(--grey-tile);display:flex;align-items:center;justify-content:center}
.tile.on{background:var(--blue)}
.tile svg{width:40px;height:40px;fill:none;stroke:var(--white);stroke-width:2.4;stroke-linecap:round;stroke-linejoin:round}
.label{width:130px;text-align:center;font-size:12px;font-weight:700;line-height:15.5px;color:#222}
.label.on{color:var(--blue)}

/* footer */
.footer{left:0;top:921px;width:910px;height:241px;background:var(--footer)}
.f-head{top:945px;color:var(--white);font-size:14px;font-weight:700}
.links{left:76px;top:970px;list-style:none}
.links li{color:var(--muted);font-size:10px;line-height:17.6px;display:flex;align-items:center;gap:8px}
.links li::before{content:"";width:5px;height:5px;border-radius:50%;background:#9a9a9d;box-shadow:0 0 0 1.5px #7b7b7e}
.cal{left:214px;top:972px;width:152px;background:var(--white)}
.cal-head{height:20px;background:var(--blue);color:var(--white);font-size:12px;font-weight:700;display:flex;justify-content:space-between;align-items:center;padding:0 6px}
.cal table{width:100%;border-collapse:collapse;table-layout:fixed;font-size:8px;text-align:center}
.cal td,.cal th{border:1px solid #ddd;height:15.4px;font-weight:400;color:#222}
.cal th{background:#f2f2f2}
.cal .sun{color:var(--red)}
.field{left:414px;width:182px;height:24px;background:var(--white);font-size:10px;color:#666;padding:7px 8px}
.select-btn{right:0;top:0;width:23px;height:24px;background:#ccc;display:flex;align-items:center;justify-content:center}
.submit{left:414px;top:1112px;width:65px;height:26px;background:var(--blue);color:var(--white);font-size:11px;font-weight:700;text-align:center;line-height:26px}
.map{left:643px;top:972px;width:192px;height:132px;background:linear-gradient(135deg,#eeeae2,#dcd8cf)}
.bottom{left:0;top:1162px;width:910px;height:38px;background:var(--footer-dark)}
.copy{left:75px;top:1176px;font-size:8.5px;color:var(--white)}
.social{right:74px;top:1169px;display:flex;gap:8px}
.social i{width:24px;height:24px;border-radius:50%;background:var(--blue)}
</style>
</head>
<body>

<header>
  <div class="abs brand">
    <div class="brand-mark"><span class="brand-dot"></span><span class="brand-name">Vanto</span></div>
    <div class="brand-sub">Vanto Events Management</div>
  </div>
  <div class="abs contact">
    <span><i class="ico"><svg width="12" height="9" viewBox="0 0 12 9"><rect x=".5" y=".5" width="11" height="8" fill="none" stroke="#fff"/><path d="M.5 .5 6 5 11.5 .5" fill="none" stroke="#fff"/></svg></i>info@vantoevents.com</span>
    <span><i class="ico"><svg width="11" height="11" viewBox="0 0 24 24"><path fill="#fff" d="M6.6 10.8a15 15 0 0 0 6.6 6.6l2.2-2.2c.3-.3.7-.4 1-.2 1.1.4 2.3.6 3.6.6.6 0 1 .4 1 1V20c0 .6-.4 1-1 1A17 17 0 0 1 3 4c0-.6.4-1 1-1h3.5c.6 0 1 .4 1 1 0 1.3.2 2.5.6 3.6.1.3 0 .7-.2 1z"/></svg></i>+123-555-0148</span>
  </div>
  <nav class="abs nav">
    <a class="active">Home</a><a>Who We Are</a><a>Core Values</a><a>Why Choose Us</a><a>Past Experience</a><a>Our Services</a><a>References</a><a>Contact Us</a>
  </nav>
</header>

<section>
  <div class="abs hero" role="img" aria-label="Photo of a scientific conference audience seated in a lecture hall facing a speaker at a lectern"></div>
  <svg class="abs hero-arrow" style="left:26px" width="22" height="44" viewBox="0 0 22 44"><path d="M20 2 2 22 20 42" fill="none" stroke="#fff" stroke-width="1.5"/></svg>
  <svg class="abs hero-arrow" style="right:26px" width="22" height="44" viewBox="0 0 22 44"><path d="M2 2 20 22 2 42" fill="none" stroke="#fff" stroke-width="1.5"/></svg>
  <div class="abs caption"><b>Nothing Is Impossible …..</b> Even The Word Itself Says I’m Possible.</div>
  <div class="abs dots"><i></i><i class="on"></i><i></i><i></i></div>
</section>

<section>
  <h2 class="abs svc-title">Our <span>Services</span></h2>
  <div class="abs divider"></div>
  <div class="abs divider-dot"></div>
  <p class="abs svc-intro">To and from the supplier anywhere in the world to and from the hospital, pharmacy, doctor, medical staff, lab and even the patient's residence.</p>

  <!-- row 1 -->
  <div class="abs tile" style="left:91px;top:616px"><svg viewBox="0 0 40 40"><ellipse cx="19" cy="23" rx="13" ry="10"/><circle cx="22" cy="10" r="4"/><path d="M12 32v4M26 32v4M32 21h4"/></svg></div>
  <div class="abs tile on" style="left:226px;top:616px"><svg viewBox="0 0 40 40"><path d="M8 34C14 24 26 16 32 6M8 24c8 2 14 8 16 14M14 8c2 6 8 12 16 14M12 30l6 2M16 24l6 3M22 17l5 3M26 11l4 2"/></svg></div>
  <div class="abs tile" style="left:354px;top:616px"><svg viewBox="0 0 40 40"><rect x="4" y="10" width="32" height="24" rx="2"/><rect x="15" y="6" width="10" height="6"/><circle cx="13" cy="19" r="3"/><path d="M8 28c1-4 9-4 10 0M22 18h10M22 23h10M22 28h8"/></svg></div>
  <div class="abs tile" style="left:485px;top:616px"><svg viewBox="0 0 40 40"><rect x="8" y="6" width="24" height="30"/><path d="M13 14h4M23 14h4M13 20h4M23 20h4M13 26h4M23 26h4M17 36v-5h6v5"/></svg></div>
  <div class="abs tile" style="left:609px;top:616px"><svg viewBox="0 0 40 40"><path d="M22 5h14v10h-8l-4 4v-4h-2z"/><circle cx="16" cy="18" r="3"/><circle cx="24" cy="20" r="2.5"/><path d="M10 27c1-4 11-4 12 0M20 27c1-3 8-3 9 0"/><rect x="12" y="30" width="12" height="7"/><path d="M12 30l6 4 6-4M6 12a16 16 0 0 0-2 8"/></svg></div>
  <div class="abs tile" style="left:741px;top:616px"><svg viewBox="0 0 40 40"><rect x="9" y="5" width="22" height="27" rx="4"/><path d="M9 18h22M14 10h12M12 36v-4M28 36v-4"/><circle cx="14" cy="25" r="1.5"/><circle cx="26" cy="25" r="1.5"/></svg></div>

  <div class="abs label" style="left:66px;top:714px">Fund Raising</div>
  <div class="abs label on" style="left:200px;top:714px">Transportation</div>
  <div class="abs label" style="left:330px;top:714px">Accreditation</div>
  <div class="abs label" style="left:460px;top:714px">Accommodations</div>
  <div class="abs label" style="left:585px;top:714px">Social Activities</div>
  <div class="abs label" style="left:715px;top:716px">Transportation</div>

  <!-- row 2 -->
  <div class="abs tile" style="left:91px;top:761px"><svg viewBox="0 0 40 40"><path d="M4 26v-6l5-2 4-7h14l4 7 5 2v6z"/><path d="M11 18h18M6 30v3h5v-3M29 30v3h5v-3"/><circle cx="10" cy="22" r="1.5"/><circle cx="30" cy="22" r="1.5"/></svg></div>
  <div class="abs tile" style="left:226px;top:761px"><svg viewBox="0 0 40 40"><circle cx="11" cy="8" r="3"/><circle cx="29" cy="8" r="3"/><path d="M11 13v14M29 13v14M7 36l4-9 4 9M25 36l4-9 4 9M11 18l7 3M29 18l-7 3M17 9h6M20 6l3 3-3 3"/></svg></div>
  <div class="abs tile" style="left:354px;top:761px"><svg viewBox="0 0 40 40"><path d="M6 14h22l6 6H12z"/><path d="M6 22h28M6 26h28M6 30h28M6 34h28M12 8h16"/></svg></div>
  <div class="abs tile" style="left:485px;top:761px"><svg viewBox="0 0 40 40"><rect x="6" y="13" width="28" height="20" rx="2"/><path d="M15 13V8h10v5M6 22h28M18 22v3h4v-3"/></svg></div>
  <div class="abs tile" style="left:609px;top:761px"><svg viewBox="0 0 40 40"><path d="M20 5a10 10 0 0 0-6 18v5h12v-5a10 10 0 0 0-6-18zM15 32h10M17 36h6M17 20l3-4 3 4"/></svg></div>
  <div class="abs tile" style="left:741px;top:761px"><svg viewBox="0 0 40 40"><path d="M20 20v16M9 28a14 14 0 1 1 22 0M14 23a8 8 0 1 1 12 0"/><circle cx="20" cy="18" r="2"/></svg></div>

  <div class="abs label" style="left:66px;top:861px">Scientific Program<br>Duties</div>
  <div class="abs label" style="left:200px;top:861px">Marketing of<br>The Event</div>
  <div class="abs label" style="left:330px;top:861px">Publications And<br>Printed Materials</div>
  <div class="abs label" style="left:458px;top:861px">Secretarial<br>Work</div>
  <div class="abs label" style="left:585px;top:861px">Marketing Of<br>The Event</div>
  <div class="abs label" style="left:715px;top:861px">Media<br>Coverage</div>
</section>

<footer>
  <div class="abs footer"></div>
  <h3 class="abs f-head" style="left:76px">Quick Links</h3>
  <h3 class="abs f-head" style="left:214px">Calendar</h3>
  <h3 class="abs f-head" style="left:414px">Quick Inquiry</h3>
  <h3 class="abs f-head" style="left:644px">Location Map</h3>

  <ul class="abs links">
    <li>Home</li><li>Who We Are</li><li>Core Values</li><li>Why Choose Us</li><li>Past Experience</li><li>Our Services</li><li>References</li><li>Contact Us</li>
  </ul>

  <div class="abs cal">
    <div class="cal-head"><span>‹</span><span>January-2016</span><span>›</span></div>
    <table>
      <tr><th class="sun">Sun</th><th>Mon</th><th>Tue</th><th>Wed</th><th>Thu</th><th>Fri</th><th>Sat</th></tr>
      <tr><td></td><td></td><td></td><td></td><td></td><td>1</td><td>2</td></tr>
      <tr><td class="sun">3</td><td>4</td><td>5</td><td>6</td><td>7</td><td>8</td><td>9</td></tr>
      <tr><td class="sun">10</td><td>11</td><td>12</td><td>13</td><td>14</td><td>15</td><td>16</td></tr>
      <tr><td class="sun">17</td><td>18</td><td>19</td><td>20</td><td>21</td><td>22</td><td>23</td></tr>
      <tr><td class="sun">24</td><td>25</td><td>26</td><td>27</td><td>28</td><td>29</td><td>30</td></tr>
      <tr><td class="sun">31</td><td></td><td></td><td></td><td></td><td></td><td></td></tr>
    </table>
  </div>

  <div class="abs field" style="top:972px">Name</div>
  <div class="abs field" style="top:1001px">Email Address</div>
  <div class="abs field" style="top:1030px">Services
    <span class="abs select-btn"><svg width="10" height="6" viewBox="0 0 10 6"><path d="M1 1 5 5 9 1" fill="none" stroke="#555" stroke-width="2"/></svg></span>
  </div>
  <div class="abs field" style="top:1060px;height:44px">Message</div>
  <div class="abs submit">SUBMIT</div>

  <div class="abs map" role="img" aria-label="Street map showing the office location"></div>

  <div class="abs bottom"></div>
  <p class="abs copy">Copyright © 2015 VantoEventsManagement. All Right Reserved.</p>
  <div class="abs social" aria-label="Social links"><i></i><i></i><i></i></div>
</footer>

</body>
</html>
```